Presentation Folder for dental clinic

We need a presentation folder design. The presentation folder is what we give to our patients with treatment plans, quotes, images, information sheets etc.
I have uploaded current stationary designs for assistance as well as a photo of our external sign design.
We are an upmarket dental clinic.
Professionalism and customer service is key to us.
We provide information in presentation folders to give to patients.
It needs to memorable and a statement to who we are.

Target Market(s)

Main patient base is Male and Female 40 years old to 70 years old

Industry/Entity Type

Dental Clinic

Font styles to use
Serif
Sans Serif

Requirements
Must have
• Design:
• -Professional
• -Timeless
• -Modern
• - Memorable
• - Statement (if a patient puts down the folder, it will be easily identifiable with as Corvel Dentals folder)
• Logo
• Address, phone, email, website
• Dr Leo Brandt name and degree details
• Colour scheme to match current logos and branding
• "Your Smile Our Passion" quote
Nice to have
• Services listed:
• - Sleep Dentistry
• - Happy Gas
• - Dental Implants
• - Cosmetic Dentistry
• - Oral Surgery
• - Alignora
• - Teeth Whitening
• - General Dentistry
• - Childrens Dentistry
• See website www.corveldental-example.com.au
Should not have
• Dental cliche photos

```html
<!DOCTYPE html>
<html lang="en">
<head>
<meta charset="utf-8">
<title>Corvel Dentals – Presentation Folder</title>
<link rel="stylesheet" href="https://fonts.googleapis.com/css2?family=Arimo:wght@400;700&family=Tinos:wght@400;700&display=swap">
<style>
  :root {
    --purple: #944a94;
    --grey: #a7a7aa;
    --slate: #6f8090;
    --white: #ffffff;
    --paper: #f7f7f7;
    --ink: #333333;
    --stage: #c4dbe6;
    --sans: "Arimo", Arial, sans-serif;
    --serif: "Tinos", "Times New Roman", serif;
  }
  html, body { margin: 0; padding: 0; overflow: hidden; }
  body { width: 1200px; height: 816px; background: var(--stage); font-family: var(--sans); }
  .canvas { position: relative; width: 1200px; height: 816px; overflow: hidden; }

  .panel { position: absolute; top: 158px; width: 360px; height: 500px; overflow: hidden; box-shadow: 0 6px 18px rgba(40,70,90,.18); }
  .panel svg.shapes { position: absolute; inset: 0; }
  .inside-left { left: 40px; }
  .inside-right { left: 400px; }
  .cover { left: 800px; }

  /* inside left */
  .tagline { position: absolute; top: 30px; right: 22px; margin: 0; font-size: 21px; font-weight: 700; color: var(--grey); }
  .tagline .accent { color: var(--purple); }
  .contact-address, .contact-web { position: absolute; bottom: 18px; margin: 0; font-size: 7.5px; line-height: 1.5; color: var(--white); }
  .contact-address { left: 16px; }
  .contact-web { right: 16px; text-align: right; }

  /* inside right: letter sheet */
  .letter { position: absolute; left: 30px; top: 30px; width: 190px; padding: 14px 20px; font-family: var(--serif); color: var(--ink); }
  .letter-mark { width: 26px; height: 26px; border-radius: 50%; background: #2f9be0; margin-bottom: 12px; }
  .letter h2 { font-size: 8.5px; margin: 0 0 8px; }
  .letter p { font-size: 7.5px; line-height: 1.5; margin: 0 0 8px; }

  /* cover */
  .brand { position: absolute; top: 46px; left: 20px; margin: 0; font-size: 30px; font-weight: 700; color: var(--purple); letter-spacing: -.5px; }
  .doctor { position: absolute; top: 150px; left: 22px; color: var(--white); }
  .doctor h2 { margin: 0 0 4px; font-size: 14px; font-weight: 700; }
  .doctor p { margin: 0; font-size: 7px; line-height: 1.45; }
  .services { position: absolute; top: 300px; left: 22px; margin: 0; padding: 0; list-style: none; }
  .services li { display: flex; align-items: center; gap: 7px; font-size: 9px; font-weight: 700; color: var(--white); line-height: 1.75; }
  .services li::before { content: ""; width: 8px; height: 8px; border-radius: 50%; background: #c9c9cc; }
</style>
</head>
<body>
<main class="canvas">

  <section class="panel inside-left" aria-label="Folder inside left panel">
    <svg class="shapes" width="360" height="500" viewBox="0 0 360 500">
      <defs>
        <linearGradient id="pattern-tone" x1="0" y1="0" x2="1" y2="1">
          <stop offset="0" stop-color="#ffffff" stop-opacity="0"/>
          <stop offset="1" stop-color="#ffffff" stop-opacity=".12"/>
        </linearGradient>
        <linearGradient id="pattern-tone-light" x1="0" y1="0" x2="1" y2="1">
          <stop offset="0" stop-color="#d8d8dc" stop-opacity=".35"/>
          <stop offset="1" stop-color="#d8d8dc" stop-opacity="0"/>
        </linearGradient>
      </defs>
      <rect width="360" height="500" fill="var(--white)"/>
      <rect x="0" y="70" width="120" height="140" fill="url(#pattern-tone-light)" role="img" aria-label="Faint geometric line pattern"/>
      <polygon points="360,70 360,500 0,500 0,420" fill="var(--purple)"/>
      <rect x="190" y="340" width="150" height="150" fill="url(#pattern-tone)" role="img" aria-label="Faint geometric line pattern"/>
    </svg>
    <h1 class="tagline">Your Smile <span class="accent">Our Passion</span></h1>
    <p class="contact-address">48 Larkfield Road, Larkfield Vic 3999<br>email: info@corveldental-example.com.au</p>
    <p class="contact-web">website: www.corveldental-example.com.au<br>phone 02 5550 1847</p>
  </section>

  <section class="panel inside-right" aria-label="Folder inside right panel with pocket">
    <svg class="shapes" width="360" height="500" viewBox="0 0 360 500">
      <rect width="360" height="500" fill="var(--purple)"/>
      <rect x="30" y="30" width="230" height="450" fill="var(--paper)"/>
    </svg>
    <article class="letter">
      <div class="letter-mark"></div>
      <h2>Welcome to our practice.</h2>
      <p>Thank you for choosing our clinic. This folder holds your treatment plan, quotes and care notes so you can review every step at home.</p>
      <p>Please read each sheet carefully and bring any questions to your next visit. Our team will gladly explain every option in plain terms.</p>
      <p>We look forward to caring for your smile for many years.</p>
    </article>
    <svg class="shapes" width="360" height="500" viewBox="0 0 360 500">
      <polygon points="245,20 350,20 360,500 0,500 0,345 245,325" fill="var(--slate)"/>
    </svg>
  </section>

  <section class="panel cover" aria-label="Folder front cover">
    <svg class="shapes" width="360" height="500" viewBox="0 0 360 500">
      <rect width="360" height="500" fill="var(--white)"/>
      <polygon points="150,100 360,40 360,92 250,118" fill="var(--grey)"/>
      <polygon points="0,135 250,125 360,100 360,500 0,500" fill="var(--purple)"/>
      <polygon points="250,500 360,410 360,500" fill="var(--grey)"/>
    </svg>
    <p class="brand">Corvel Dental</p>
    <div class="doctor">
      <h2>Dr Leo Brandt &amp; Associates</h2>
      <p>B.D.S. Honours, Clinical Dentistry<br>Graduate Certificate Oral Implants<br>Member Dental Practice Association</p>
    </div>
    <ul class="services">
      <li>Sleep Dentistry</li>
      <li>Happy Gas</li>
      <li>Dental Implants</li>
      <li>Cosmetic Dentistry</li>
      <li>Oral Surgery</li>
      <li>Alignora</li>
      <li>Teeth Whitening</li>
      <li>General Dentistry</li>
      <li>Childrens Dentistry</li>
    </ul>
  </section>

</main>
</body>
</html>
```